Tavrinel House

I am looking at a A4 one sided fact sheet about the property I developed, which I can print off or send electronically
Our current logo is Navy blue and Maroon colors
House

```html
<!DOCTYPE html>
<html lang="en">
<head>
<meta charset="utf-8">
<title>Tavrinel House – Project Fact Sheet</title>
<link href="https://fonts.googleapis.com/css2?family=Fira+Sans:wght@400;600;700;800&family=Fira+Sans+Condensed:wght@400;600;700&family=Montserrat:wght@400;500;600;700&display=swap" rel="stylesheet">
<style>
  :root{
    --navy:#1b2457;
    --navy-dark:#141b44;
    --maroon:#8e1b26;
    --maroon-dark:#6f121b;
    --paper:#f4f4f5;
    --ink:#2b2b2b;
    --canvas:#e3e3e3;
  }
  *{margin:0;padding:0;box-sizing:border-box}
  html,body{width:1155px;height:1200px;overflow:hidden;background:var(--canvas)}
  .sheet{position:absolute;left:153px;top:0;width:848px;height:1200px;background:var(--paper);overflow:hidden;font-family:"Fira Sans Condensed",sans-serif;color:var(--ink)}

  /* header */
  .header{position:absolute;left:0;top:0;width:848px;height:128px;background:#ececee}
  .header-band{position:absolute;left:0;top:0}
  .brand-name{position:absolute;left:44px;top:38px;width:230px;color:var(--navy);font-family:"Montserrat",sans-serif;font-weight:600;font-size:25px;line-height:1.2}
  .phone-block{position:absolute;left:350px;top:16px;width:200px;text-align:center;color:#fff;font-family:"Montserrat",sans-serif}
  .phone-block .label{font-size:12.5px;font-weight:600;margin-top:10px}
  .phone-block .number{font-size:28px;font-weight:700;line-height:1.05}
  .hex{display:block;margin:0 auto}
  .divider{position:absolute;left:552px;top:22px;width:1px;height:84px;background:rgba(255,255,255,.35)}
  .contact{position:absolute;left:575px;color:#fff;font-family:"Montserrat",sans-serif;font-size:11.5px;line-height:16px;display:flex;gap:10px;align-items:flex-start}
  .contact svg{flex:none;margin-top:2px}
  .header-rule{position:absolute;left:0;top:128px;width:848px;height:7px;background:var(--navy)}

  /* hero */
  .hero{position:absolute;left:0;top:135px;width:848px;height:440px;background:linear-gradient(180deg,#4e6fa8 0%,#8ea6cb 40%,#7a6a62 62%,#4b4340 100%)}
  .arc{position:absolute;left:0;top:500px}

  /* thumbnails */
  .thumb{position:absolute;top:527px;width:243px;height:193px;box-shadow:0 4px 8px rgba(0,0,0,.25)}
  .thumb .photo{position:absolute;left:7px;top:7px;right:7px;height:150px}
  .thumb .caption{position:absolute;left:0;bottom:0;width:100%;height:36px;color:#fff;font-family:"Montserrat",sans-serif;font-weight:700;font-size:17.5px;text-align:center;line-height:36px}
  .thumb-navy{background:var(--navy)}
  .thumb-maroon{background:var(--maroon)}
  .gym .photo{background:linear-gradient(160deg,#c9ccd0 0%,#b4444d 35%,#6f7480 70%,#3a3d44 100%)}
  .boardroom .photo{background:linear-gradient(180deg,#a7825a 0%,#e6e2d8 40%,#7b7a78 75%,#3b3d43 100%)}
  .lounge .photo{background:linear-gradient(180deg,#9a7a55 0%,#e7e5df 45%,#8fa48a 70%,#5c5e63 100%)}

  /* strategy */
  .strategy{position:absolute;left:34px;top:757px;width:368px}
  .section-title{font-family:"Fira Sans",sans-serif;font-weight:800;font-size:29px;color:var(--maroon);letter-spacing:.2px;padding-bottom:8px;border-bottom:1.5px solid #bdbdbd}
  .strategy p{font-size:12.6px;line-height:17.1px;text-align:justify;margin-top:20px}
  .strategy p + p{margin-top:16px}
  .strategy b{font-weight:700;color:#1a1a1a}
  .column-rule{position:absolute;left:420px;top:760px;width:1px;height:300px;background:#d4d4d4}

  /* fact sheet */
  .facts{position:absolute;left:438px;top:762px;width:386px;height:288px;background:#f0f0f1;box-shadow:0 3px 8px rgba(0,0,0,.22)}
  .facts-head{height:46px;background:var(--navy);color:#fff;font-family:"Fira Sans",sans-serif;font-weight:700;font-size:24px;display:flex;align-items:center;justify-content:center;gap:16px}
  .facts ul{list-style:none;padding:12px 0 0 12px}
  .facts li{display:flex;align-items:center;gap:9px;font-size:14.4px;height:27.2px;color:#1f1f1f;white-space:nowrap}
  .facts li strong{color:var(--maroon);font-weight:700;margin-right:4px}

  /* footer */
  .tagline{position:absolute;left:0;top:1083px}
  .tagline-text{position:absolute;left:0;top:1088px;width:848px;text-align:center;color:#fff;font-family:"Fira Sans",sans-serif;font-weight:800;font-size:33px;letter-spacing:-.2px}
  .footer-bar{position:absolute;left:0;top:1147px;width:848px;height:32px;background:var(--navy);display:flex;align-items:center;justify-content:space-around;padding:0 30px;color:#fff;font-family:"Montserrat",sans-serif;font-weight:600;font-size:13.5px}
  .footer-bar span{display:flex;align-items:center;gap:10px}
  .footer-base{position:absolute;left:0;top:1179px}
</style>
</head>
<body>
<main class="sheet">

  <header class="header">
    <svg class="header-band" width="848" height="128" viewBox="0 0 848 128" aria-hidden="true">
      <polygon points="258,0 848,0 848,128 330,128" fill="var(--maroon)"/>
    </svg>
    <div class="brand-name">Meridale Development</div>
    <div class="phone-block">
      <svg class="hex" width="40" height="44" viewBox="0 0 40 44" aria-hidden="true">
        <polygon points="20,1 38,11 38,33 20,43 2,33 2,11" fill="var(--maroon-dark)"/>
        <rect x="14" y="11" width="12" height="21" rx="2" fill="none" stroke="#fff" stroke-width="2"/>
        <circle cx="20" cy="28" r="1.3" fill="#fff"/>
      </svg>
      <div class="label">FOR MORE INFORMATION</div>
      <div class="number">0400 555 218</div>
    </div>
    <div class="divider"></div>
    <div class="contact" style="top:26px">
      <svg width="26" height="26" viewBox="0 0 26 26" aria-hidden="true"><circle cx="13" cy="13" r="13" fill="#fff"/><path d="M13 5a5 5 0 0 0-5 5c0 4 5 10 5 10s5-6 5-10a5 5 0 0 0-5-5z" fill="var(--maroon)"/><circle cx="13" cy="10" r="2" fill="#fff"/></svg>
      <div>Level 1, 40 Harbour St, GPO Box 1180,<br>Brisbane, Queensland, 4000.</div>
    </div>
    <div class="contact" style="top:78px">
      <svg width="26" height="26" viewBox="0 0 26 26" aria-hidden="true"><circle cx="13" cy="13" r="13" fill="#fff"/><circle cx="13" cy="13" r="7" fill="none" stroke="var(--maroon)" stroke-width="1.6"/><path d="M6 13h14M13 6c-3 4-3 10 0 14M13 6c3 4 3 10 0 14" fill="none" stroke="var(--maroon)" stroke-width="1.3"/></svg>
      <div>enquiries@meridaledev.com.au<br>www.meridaledev.com.au</div>
    </div>
  </header>
  <div class="header-rule"></div>

  <div class="hero" role="img" aria-label="Photograph of Tavrinel House, a six-storey commercial office building at dusk"></div>

  <svg class="arc" width="848" height="80" viewBox="0 0 848 80" aria-hidden="true">
    <path d="M0 58 Q424 -22 848 58 L848 80 L0 80 Z" fill="var(--maroon)"/>
    <path d="M0 66 Q424 -12 848 66 L848 80 L0 80 Z" fill="var(--paper)"/>
  </svg>

  <section class="thumb thumb-navy gym" style="left:50px">
    <div class="photo" role="img" aria-label="Photograph of the gym with exercise equipment"></div>
    <div class="caption">MULTY GYM</div>
  </section>
  <section class="thumb thumb-maroon boardroom" style="left:304px">
    <div class="photo" role="img" aria-label="Photograph of a boardroom with a long table and leather chairs"></div>
    <div class="caption">OFFICE BUILDING</div>
  </section>
  <section class="thumb thumb-navy lounge" style="left:561px">
    <div class="photo" role="img" aria-label="Photograph of an open lounge area with timber ceiling"></div>
    <div class="caption">LIVING ROOM</div>
  </section>

  <section class="strategy">
    <h2 class="section-title">DEVELOPMENT STRATEGY</h2>
    <p><b>Tavrinel</b> is a world class mining engineering firm.They had 6 offices spread out of a number of locations in the Southern part of Brisbane. Working with Tavrinel, we identified a site for their new headquarters. We purchased the land and applied for a development approval to develop a <b>15,700m2</b> office building on the site. We designed an office building around their requirements including their staff requirements, gym, bike rack, change rooms, outdoor dining areas, café, large car parking facility, storage etc.</p>
    <p>We appointed Carrow Builders to undertake a “design and construct” contract to build the development. Construction lasted about <b>18 months</b> and we completed an integrated fitout to get them into the office space quicker. The property was sold on completion to American based fund manager Valdren for <b>$87.2m</b></p>
  </section>
  <div class="column-rule"></div>

  <section class="facts">
    <h2 class="facts-head">
      <svg width="13" height="13" viewBox="0 0 24 24" aria-hidden="true"><polygon points="12,1 15,9 23,9 17,14 19,23 12,18 5,23 7,14 1,9 9,9" fill="#fff"/></svg>
      PROJECT FACT SHEET
      <svg width="13" height="13" viewBox="0 0 24 24" aria-hidden="true"><polygon points="12,1 15,9 23,9 17,14 19,23 12,18 5,23 7,14 1,9 9,9" fill="#fff"/></svg>
    </h2>
    <ul>
      <li><svg width="16" height="16" viewBox="0 0 16 16" aria-hidden="true"><circle cx="8" cy="8" r="8" fill="var(--maroon)"/><path d="M4.3 8.2l2.5 2.4 4.9-5" fill="none" stroke="#fff" stroke-width="1.9"/></svg><span><strong>Name:</strong> Tavrinel House</span></li>
      <li><svg width="16" height="16" viewBox="0 0 16 16" aria-hidden="true"><circle cx="8" cy="8" r="8" fill="var(--maroon)"/><path d="M4.3 8.2l2.5 2.4 4.9-5" fill="none" stroke="#fff" stroke-width="1.9"/></svg><span><strong>Address:</strong> 58 Riverbend Road South Brisbane</span></li>
      <li><svg width="16" height="16" viewBox="0 0 16 16" aria-hidden="true"><circle cx="8" cy="8" r="8" fill="var(--maroon)"/><path d="M4.3 8.2l2.5 2.4 4.9-5" fill="none" stroke="#fff" stroke-width="1.9"/></svg><span><strong>When Developed:</strong> 2008</span></li>
      <li><svg width="16" height="16" viewBox="0 0 16 16" aria-hidden="true"><circle cx="8" cy="8" r="8" fill="var(--maroon)"/><path d="M4.3 8.2l2.5 2.4 4.9-5" fill="none" stroke="#fff" stroke-width="1.9"/></svg><span><strong>Value on Completion:</strong> $87m</span></li>
      <li><svg width="16" height="16" viewBox="0 0 16 16" aria-hidden="true"><circle cx="8" cy="8" r="8" fill="var(--maroon)"/><path d="M4.3 8.2l2.5 2.4 4.9-5" fill="none" stroke="#fff" stroke-width="1.9"/></svg><span><strong>Size:</strong> 15,700m2 NLA</span></li>
      <li><svg width="16" height="16" viewBox="0 0 16 16" aria-hidden="true"><circle cx="8" cy="8" r="8" fill="var(--maroon)"/><path d="M4.3 8.2l2.5 2.4 4.9-5" fill="none" stroke="#fff" stroke-width="1.9"/></svg><span><strong>Type of Property:</strong> A Grade Commercial Office Space</span></li>
      <li><svg width="16" height="16" viewBox="0 0 16 16" aria-hidden="true"><circle cx="8" cy="8" r="8" fill="var(--maroon)"/><path d="M4.3 8.2l2.5 2.4 4.9-5" fill="none" stroke="#fff" stroke-width="1.9"/></svg><span><strong>Quality rating:</strong> 4 Star</span></li>
      <li><svg width="16" height="16" viewBox="0 0 16 16" aria-hidden="true"><circle cx="8" cy="8" r="8" fill="var(--maroon)"/><path d="M4.3 8.2l2.5 2.4 4.9-5" fill="none" stroke="#fff" stroke-width="1.9"/></svg><span><strong>Developed by:</strong> Meridale Development Corporation Pty Ltd</span></li>
    </ul>
  </section>

  <svg class="tagline" width="848" height="64" viewBox="0 0 848 64" aria-hidden="true">
    <polygon points="86,0 762,0 808,64 40,64" fill="var(--maroon)"/>
  </svg>
  <div class="tagline-text">PROPERTY DEVELOPERS &amp; INVESTORS</div>

  <footer class="footer-bar">
    <span><svg width="17" height="12" viewBox="0 0 17 12" aria-hidden="true"><rect x=".5" y=".5" width="16" height="11" fill="#fff"/><path d="M.5 .5l8 6 8-6" fill="none" stroke="var(--navy)" stroke-width="1.3"/></svg>TEAM@MERIDALEDEV.COM.AU</span>
    <span><svg width="16" height="16" viewBox="0 0 24 24" aria-hidden="true"><path d="M6.6 10.8a15 15 0 0 0 6.6 6.6l2.2-2.2c.3-.3.7-.4 1-.2 1.1.4 2.3.6 3.6.6.6 0 1 .4 1 1V20c0 .6-.4 1-1 1A17 17 0 0 1 3 4c0-.6.4-1 1-1h3.5c.6 0 1 .4 1 1 0 1.3.2 2.5.6 3.6.1.3 0 .7-.2 1z" fill="#fff"/></svg>0400 555 218</span>
    <span><svg width="16" height="16" viewBox="0 0 24 24" aria-hidden="true"><circle cx="12" cy="12" r="10" fill="none" stroke="#fff" stroke-width="2"/><path d="M2 12h20M12 2c-4 5-4 15 0 20M12 2c4 5 4 15 0 20" fill="none" stroke="#fff" stroke-width="1.6"/></svg>WWW.MERIDALEDEV.COM.AU</span>
  </footer>
  <svg class="footer-base" width="848" height="21" viewBox="0 0 848 21" aria-hidden="true">
    <rect width="848" height="21" fill="var(--paper)"/>
    <polygon points="20,0 828,0 810,21 38,21" fill="var(--maroon)"/>
  </svg>

</main>
</body>
</html>
```